The Harvest Compass

Cutting Through the Noise to What Actually Works.

Nutrition book

Target Market(s)

People looking to be or get healthy and eat right.

```html
<!DOCTYPE html>
<html lang="en">
<head>
<meta charset="utf-8">
<title>The Harvest Compass — Nutrition Book</title>
<link rel="stylesheet" href="https://fonts.googleapis.com/css2?family=Anton&family=Caveat:wght@500&family=Nunito:wght@600;900&family=Oswald:wght@600;700&display=swap">
<style>
  :root {
    --sky-top: #dcebf5;
    --sky-bottom: #c4e0f4;
    --ink-purple: #3a2190;
    --accent-orange: #f7931e;
    --band-purple: #3a2190;
    --white: #ffffff;
    --tier-gold: #f6c12f;
    --tier-orange: #f08a24;
    --tier-green: #3f9a2f;
    --tier-blue: #1f7fd4;
    --tier-violet: #5b2fc7;
    --tier-navy: #1f2f4f;
  }
  * { margin: 0; padding: 0; box-sizing: border-box; }
  html, body { width: 800px; height: 1200px; overflow: hidden; }
  body {
    position: relative;
    background: linear-gradient(180deg, var(--sky-top) 0%, var(--sky-top) 55%, var(--sky-bottom) 100%);
    font-family: "Nunito", sans-serif;
  }
  .cover-title { position: absolute; left: 0; top: 0; width: 800px; height: 580px; text-align: center; }
  .title-article {
    position: absolute; left: 0; width: 800px; top: 34px;
    font-family: "Caveat", cursive; font-weight: 500; font-size: 108px;
    color: var(--accent-orange); line-height: 1; text-align: center;
  }
  .title-line {
    position: absolute; left: 0; width: 800px;
    font-family: "Anton", sans-serif; font-weight: 400; line-height: 1;
    text-align: center; transform: scaleX(1.12); transform-origin: 50% 50%;
  }
  .title-line--first {
    top: 171px; font-size: 163px; letter-spacing: 8px; padding-left: 8px;
    color: var(--ink-purple);
  }
  .title-line--second {
    top: 340px; font-size: 133px; letter-spacing: 18px; padding-left: 18px;
    color: var(--accent-orange);
  }
  .tagline {
    position: absolute; left: 0; width: 800px; top: 460px;
    font-family: "Oswald", sans-serif; font-weight: 700; font-size: 46px;
    line-height: 54px; color: var(--ink-purple); text-align: center;
    text-transform: uppercase; letter-spacing: -0.8px;
    transform: scaleX(0.86); transform-origin: 50% 50%;
  }
  .tagline em { font-style: normal; color: var(--accent-orange); }
  .hierarchy { position: absolute; left: 0; top: 600px; width: 800px; height: 520px; }
  .tier-label-title { font-family: "Nunito", sans-serif; font-weight: 900; font-size: 17px; fill: var(--ink-purple); }
  .tier-label-sub { font-family: "Nunito", sans-serif; font-weight: 600; font-size: 11.5px; fill: var(--ink-purple); }
  .tier-number { font-family: "Nunito", sans-serif; font-weight: 900; font-size: 20px; fill: var(--white); }
  .footer-band {
    position: absolute; left: 0; top: 1128px; width: 800px; height: 72px;
    background: var(--band-purple);
    display: flex; align-items: center; justify-content: center;
  }
  .footer-label {
    font-family: "Oswald", sans-serif; font-weight: 600; font-size: 37px;
    color: var(--white); letter-spacing: 10px; text-transform: uppercase;
  }
</style>
</head>
<body>
  <header class="cover-title">
    <div class="title-article">The</div>
    <h1 class="title-line title-line--first">HARVEST</h1>
    <div class="title-line title-line--second">COMPASS</div>
    <p class="tagline">Cutting through the noise to what<br>actually <em>works</em></p>
  </header>

  <svg class="hierarchy" viewBox="0 600 800 520" xmlns="http://www.w3.org/2000/svg">
    <defs>
      <linearGradient id="g-gold" x1="0" y1="0" x2="0" y2="1"><stop offset="0" stop-color="#fde27a"/><stop offset="1" stop-color="#f0a81c"/></linearGradient>
      <linearGradient id="g-orange" x1="0" y1="0" x2="0" y2="1"><stop offset="0" stop-color="#f7a84a"/><stop offset="1" stop-color="#e2731a"/></linearGradient>
      <linearGradient id="g-green" x1="0" y1="0" x2="0" y2="1"><stop offset="0" stop-color="#6cbf3f"/><stop offset="1" stop-color="#2f7e27"/></linearGradient>
      <linearGradient id="g-blue" x1="0" y1="0" x2="0" y2="1"><stop offset="0" stop-color="#3aa3ee"/><stop offset="1" stop-color="#1464bf"/></linearGradient>
      <linearGradient id="g-violet" x1="0" y1="0" x2="0" y2="1"><stop offset="0" stop-color="#7a4be0"/><stop offset="1" stop-color="#4622a8"/></linearGradient>
      <linearGradient id="g-navy" x1="0" y1="0" x2="0" y2="1"><stop offset="0" stop-color="#34476e"/><stop offset="1" stop-color="#16213a"/></linearGradient>
    </defs>

    <g role="img" aria-label="Top tier: flame and lightning symbol for energy">
      <polygon points="300,620 360,710 238,710" fill="url(#g-gold)"/>
    </g>
    <g role="img" aria-label="Protein tier: salmon, chicken, eggs and beans">
      <polygon points="225,716 372,716 410,782 188,782" fill="url(#g-orange)"/>
    </g>
    <g role="img" aria-label="Whole foods tier: vegetables, fruit, nuts and grains">
      <polygon points="180,786 412,786 452,854 142,854" fill="url(#g-green)"/>
    </g>
    <g role="img" aria-label="Meal timing tier: three plated meals with clocks">
      <polygon points="135,858 455,858 492,930 95,930" fill="url(#g-blue)"/>
    </g>
    <g role="img" aria-label="Supplements tier: protein tub, fish oil capsules, vitamin bottle and pills">
      <polygon points="90,934 498,934 530,998 55,998" fill="url(#g-violet)"/>
    </g>
    <g role="img" aria-label="Base tier: phones, laptops, television and sound switched off">
      <polygon points="50,1002 535,1002 572,1070 28,1070" fill="url(#g-navy)"/>
    </g>

    <g>
      <circle cx="256" cy="688" r="14" fill="var(--tier-gold)" stroke="#fff" stroke-width="2"/><text class="tier-number" x="256" y="695" text-anchor="middle" font-size="16">1</text>
      <circle cx="201" cy="750" r="16" fill="var(--tier-orange)" stroke="#fff" stroke-width="2"/><text class="tier-number" x="201" y="757" text-anchor="middle">2</text>
      <circle cx="152" cy="821" r="17" fill="var(--tier-green)" stroke="#fff" stroke-width="2"/><text class="tier-number" x="152" y="828" text-anchor="middle">3</text>
      <circle cx="108" cy="893" r="18" fill="var(--tier-blue)" stroke="#fff" stroke-width="2"/><text class="tier-number" x="108" y="900" text-anchor="middle">4</text>
      <circle cx="65" cy="962" r="18" fill="var(--tier-violet)" stroke="#fff" stroke-width="2"/><text class="tier-number" x="65" y="969" text-anchor="middle">5</text>
      <circle cx="26" cy="1027" r="18" fill="var(--tier-navy)" stroke="#fff" stroke-width="2"/><text class="tier-number" x="26" y="1034" text-anchor="middle">6</text>
    </g>

    <g fill="none" stroke-width="1.5">
      <polyline points="352,675 375,660 408,660" stroke="var(--tier-gold)"/>
      <polyline points="398,742 420,730 452,730" stroke="var(--tier-orange)"/>
      <polyline points="440,810 462,800 492,800" stroke="var(--tier-green)"/>
      <polyline points="484,890 506,876 534,876" stroke="var(--tier-blue)"/>
      <polyline points="522,964 544,950 568,950" stroke="var(--tier-violet)"/>
      <polyline points="562,1030 582,1020 602,1020" stroke="var(--tier-navy)"/>
    </g>

    <g class="tier-label">
      <rect x="407" y="647" width="190" height="46" rx="23" fill="#fff8e0" stroke="var(--tier-gold)" stroke-width="1.5"/>
      <text class="tier-label-title" x="432" y="668">CALORIES</text>
      <text class="tier-label-sub" x="432" y="684">Energy for Life</text>
      <circle cx="585" cy="670" r="26" fill="var(--tier-gold)" stroke="#fff" stroke-width="3"/>
    </g>
    <g class="tier-label">
      <rect x="452" y="718" width="200" height="46" rx="23" fill="#fdebd9" stroke="var(--tier-orange)" stroke-width="1.5"/>
      <text class="tier-label-title" x="477" y="739">PROTEIN</text>
      <text class="tier-label-sub" x="477" y="755">Builds &amp; Repairs</text>
      <circle cx="640" cy="741" r="27" fill="var(--tier-orange)" stroke="#fff" stroke-width="3"/>
    </g>
    <g class="tier-label">
      <rect x="492" y="789" width="220" height="46" rx="23" fill="#e6f5dc" stroke="var(--tier-green)" stroke-width="1.5"/>
      <text class="tier-label-title" x="514" y="810">FOOD QUALITY</text>
      <text class="tier-label-sub" x="514" y="826">Choose Real, Whole Foods</text>
      <circle cx="702" cy="812" r="27" fill="var(--tier-green)" stroke="#fff" stroke-width="3"/>
    </g>
    <g class="tier-label">
      <rect x="534" y="864" width="210" height="46" rx="23" fill="#e0effc" stroke="var(--tier-blue)" stroke-width="1.5"/>
      <text class="tier-label-title" x="556" y="885">MEAL TIMING</text>
      <text class="tier-label-sub" x="556" y="901">Fuel at the Right Time</text>
      <circle cx="733" cy="887" r="27" fill="var(--tier-blue)" stroke="#fff" stroke-width="3"/>
      <circle cx="733" cy="887" r="15" fill="none" stroke="#fff" stroke-width="2.5"/>
      <polyline points="733,877 733,887 740,893" fill="none" stroke="#fff" stroke-width="2.5" stroke-linecap="round"/>
    </g>
    <g class="tier-label">
      <rect x="568" y="938" width="198" height="46" rx="23" fill="#ece4fb" stroke="var(--tier-violet)" stroke-width="1.5"/>
      <text class="tier-label-title" x="588" y="959">SUPPLEMENTS</text>
      <text class="tier-label-sub" x="588" y="975">Fill the Gaps</text>
      <circle cx="757" cy="961" r="27" fill="var(--tier-violet)" stroke="#fff" stroke-width="3"/>
    </g>
    <g class="tier-label">
      <rect x="602" y="1010" width="180" height="46" rx="23" fill="#e3e8f0" stroke="var(--tier-navy)" stroke-width="1.5"/>
      <text class="tier-label-title" x="622" y="1031">NOISE</text>
      <text class="tier-label-sub" x="622" y="1047">Reduce Distractions</text>
      <circle cx="768" cy="1033" r="27" fill="var(--tier-navy)" stroke="#fff" stroke-width="3"/>
      <polygon points="755,1028 761,1028 768,1021 768,1045 761,1038 755,1038" fill="#fff"/>
      <path d="M773,1028 l8,10 M781,1028 l-8,10" stroke="#fff" stroke-width="2.2" stroke-linecap="round"/>
    </g>
  </svg>

  <footer class="footer-band">
    <span class="footer-label">Nutrition Book</span>
  </footer>
</body>
</html>
```